Identity Package (Logo, Website)

We need a logo and website design for a new company.
The new company is a voicemail transcription service provider. It's name is KB7LUX.io
It will be very transactional. We like the "bootstrap" look and feel, and will be using a developer familiar with bootstrap. Here are the kinds of webpages we like :
https://www.plinverotrack.io
http://www.quorvix.com/
http://www.brenmoda.com/
There will only be 5 pages, as follows :
1- Homepage
2- Voicemail Transcription for Individuals
3- Voicemail Transcription for Companies
4- Wholesale Voicemail Transcription for Service Providers/Enterprises
5- Contact us
As far as the logo is concerned, we'd like to have just stylized text. It should be done in such a way as to make it easy to see the different elements of the name, which are KB, 7, and LUX.
Reason: I have received a number of designs, but the designs are mostly from the same few designers (not that much variety in designers). I'd like a few more to compare if possible, so I thought I would keep this open until Monday to give more designers the opportunity to submit over the weekend. Thanks!

```html
<!DOCTYPE html>
<html lang="en">
<head>
<meta charset="utf-8">
<title>KB7LUX.io – For Companies</title>
<link rel="stylesheet" href="https://fonts.googleapis.com/css2?family=Open+Sans:wght@400;600;700&family=Oswald:wght@500&display=swap">
<style>
:root{
  --green:#8dc63f;
  --green-dark:#7ab531;
  --ink:#222;
  --text:#555;
  --muted:#999;
  --line:#e6e6e6;
  --topbar:#3b3b3b;
  --footer:#333;
  --footer-bottom:#2a2a2a;
  --footer-text:#bbb;
  --acc-bg:#e9e9e9;
}
*{box-sizing:border-box;margin:0;padding:0}
html,body{width:935px;height:1200px;overflow:hidden}
body{font-family:"Open Sans",Arial,sans-serif;background:#fff;color:var(--text);position:relative}
.abs{position:absolute}

.topbar{left:0;top:0;width:935px;height:20px;background:var(--topbar);border-bottom:2px solid var(--green)}
.topbar .contact{left:133px;top:3px;font-size:8px;color:#aaa}
.topbar .social{right:133px;top:5px;display:flex;gap:15px}
.topbar .social span{width:9px;height:9px;border-radius:50%;background:#888;display:block}

.header{left:0;top:20px;width:935px;height:68px;background:#fff}
.logo{left:133px;top:14px;font-family:"Oswald",sans-serif;font-weight:500;font-size:27px;color:#2b2b2b;letter-spacing:.5px}
.nav{left:352px;top:0;display:flex;height:68px}
.nav a{font-size:10px;font-weight:700;color:#555;text-decoration:none;padding:0 12px;line-height:58px;height:68px;letter-spacing:.2px}
.nav a.active{color:var(--green);border-bottom:3px solid #444}

.hero{left:0;top:88px;width:935px;height:114px;background:linear-gradient(90deg,var(--green) 0%,var(--green) 60%,#9acd50 80%,#84bb3a 100%)}
.hero h1{position:absolute;left:0;width:935px;top:10px;text-align:center;font-size:50px;font-weight:600;color:#fff;letter-spacing:.5px}
.hero p{position:absolute;left:357px;top:68px;font-size:24px;color:#fff;font-weight:400;letter-spacing:.5px}

.post{left:133px;top:230px;width:486px}
.post h2{font-size:19px;font-weight:400;color:var(--ink)}
.post .meta{margin-top:6px;font-size:8.5px;color:var(--muted);display:flex;gap:14px}
.post .photo{margin-top:16px;width:486px;height:324px;background:linear-gradient(160deg,#dfe7ee 0%,#b9c6d1 35%,#5f6870 70%,#3a3f45 100%)}
.post p{font-size:9.5px;line-height:15.5px;color:#555;margin-top:8px}
.post p+p{margin-top:9px}
.btn{display:inline-block;margin-top:12px;background:var(--green);color:#fff;font-size:9px;font-weight:700;padding:5px 8px;border-radius:2px;border-bottom:2px solid var(--green-dark)}
.post-rule{left:133px;top:820px;width:486px;height:1px;background:var(--line)}

.search{left:653px;top:241px;width:160px;height:23px;border:2px solid #e3e3e3;font-size:9px;color:#aaa;padding:4px 6px}
.widget-title{font-size:10.5px;font-weight:700;color:var(--ink);letter-spacing:.3px}
.cats{left:653px;top:312px;width:160px}
.cats ul{list-style:none;margin-top:14px}
.cats li{font-size:9px;color:#555;border-bottom:1px solid #eee;height:25.3px;line-height:22px;padding-left:13px;position:relative}
.cats li:before{content:"";position:absolute;left:3px;top:10px;border-left:3px solid #777;border-top:2px solid transparent;border-bottom:2px solid transparent}
.accordion{left:653px;top:543px;width:160px}
.acc{margin-top:13px}
.acc-item{background:var(--acc-bg);border-bottom:2px solid #fff;font-size:9px;font-weight:700;color:var(--ink);padding:11px 16px;position:relative}
.acc-item .sign{position:absolute;right:14px;top:9px;color:#999;font-size:12px;font-weight:400}
.acc-item.open{background:#fff;border:3px solid #c8cfd3;color:var(--green);padding:10px 14px 12px}
.acc-item.open .sign{color:var(--green)}
.acc-item.open .body{color:#666;font-weight:400;font-size:9px;line-height:15px;margin-top:12px;padding:8px 10px 0 0;border-top:1px solid #eee}

.tweetbar{left:0;top:886px;width:935px;height:43px;background:var(--green);border-top:3px solid #ddd}
.tweetbar .bird{position:absolute;left:135px;top:14px}
.tweetbar .msg{position:absolute;left:153px;top:13px;font-size:8.5px;color:#fff}
.tweetbar .dots{position:absolute;left:776px;top:17px;display:flex;gap:4px}
.tweetbar .dots span{width:7px;height:7px;border-radius:50%;background:#3d5a1c}
.tweetbar .dots span.on{background:#fff}

.footer{left:0;top:929px;width:935px;height:224px;background:var(--footer)}
.footer .col{position:absolute;top:25px}
.f-logo{font-family:"Oswald",sans-serif;font-weight:500;font-size:24px;color:#777}
.footer .about{font-size:8.5px;line-height:15.5px;color:var(--footer-text);width:140px;margin-top:12px}
.footer h4{font-size:10.5px;font-weight:700;color:#ddd;letter-spacing:.3px;margin-top:5px}
.footer ul{list-style:none;margin-top:16px}
.footer li{font-size:8.5px;color:var(--footer-text);height:19px;padding-left:10px;position:relative}
.footer li:before{content:"›";position:absolute;left:0;top:-2px;font-size:10px}
.thumbs{display:grid;grid-template-columns:repeat(3,35px);gap:7px 6px;margin-top:14px}
.thumbs div{width:35px;height:35px}
.tags{margin-top:16px;width:170px}
.tag-row{display:flex;gap:5px;margin-bottom:6px}
.tag-row span{background:#262626;color:#ccc;font-size:7.5px;padding:4px 6px;white-space:nowrap}
.copy{left:0;top:1153px;width:935px;height:47px;background:var(--footer-bottom)}
.copy p{position:absolute;left:136px;top:19px;font-size:8px;color:#aaa}
</style>
</head>
<body>

<div class="abs topbar">
  <div class="abs contact">Call Us: (1)402 771 395 - Mail hello@kb7lux.io</div>
  <div class="abs social" aria-label="Social links"><span></span><span></span><span></span><span></span><span></span><span></span></div>
</div>

<header class="abs header">
  <div class="abs logo">KB7LUX.io</div>
  <nav class="abs nav">
    <a href="#">HOME</a>
    <a href="#">FOR INDIVIDUALS</a>
    <a href="#" class="active">FOR COMPANIES</a>
    <a href="#">FOR WHOLESELLERS</a>
    <a href="#">CONTACT</a>
  </nav>
</header>

<section class="abs hero">
  <h1>Developmental Success</h1>
  <p>and how to Achieve it.</p>
</section>

<article class="abs post">
  <h2>Sonavelle Audio with Post</h2>
  <div class="meta"><span>◷ February 12, 2013</span><span>By admin</span><span>Browsers - Desktop Viewer - Web</span><span>0 Comments</span></div>
  <div class="photo" role="img" aria-label="Photo of three businessmen talking in a bright glass office"></div>
  <p>Lorem ipsum dolor sit amet, consectetur adipiscing elit. Ut orci erat, laoreet aliquam porta a, tempor eget velit. Ut scelerisque volutpat fringilla. Sed vitae eros non mauris tempor viverra. Aliquam eget erat ac justo placerat molestie. Sed vitae.</p>
  <p>Lorem ipsum dolor sit amet, consectetur adipiscing elit. Ut orci erat, laoreet aliquam porta a, tempor eget velit. Ut scelerisque volutpat fringilla. Sed vitae eros non mauris tempor viverra. Aliquam eget erat ac justo placerat molestie. Sed vitae eros non mauris tempor viverra. Aliquam eget erat ac justo placerat molestie.Sed vitae eros non mauris tempor [...]</p>
  <span class="btn">CONTINUE READING</span>
</article>
<div class="abs post-rule"></div>

<div class="abs search">Search</div>

<aside class="abs cats">
  <h3 class="widget-title">CATEGORIES</h3>
  <ul>
    <li>Branding</li><li>Design Best Practices</li><li>Performance</li><li>Responsive Design</li><li>Typography</li><li>Uncategorized</li><li>User Experience</li>
  </ul>
</aside>

<aside class="abs accordion">
  <h3 class="widget-title">ACCORDION</h3>
  <div class="acc">
    <div class="acc-item open">Website Design<span class="sign">−</span>
      <div class="body">Lorem ipsum dolor sit amet nec, consectetuer adipiscing elit. Aenean commodo ligula eget dolor. Aenean massa. Cum sociis natoque penatibus et magnis dis parturient montes.</div>
    </div>
    <div class="acc-item">Website Development<span class="sign">+</span></div>
    <div class="acc-item">Content Management Systems<span class="sign">+</span></div>
    <div class="acc-item">E-Commerce<span class="sign">+</span></div>
  </div>
</aside>

<div class="abs tweetbar">
  <svg class="bird" width="11" height="11" viewBox="0 0 10 10"><circle cx="5" cy="5" r="4.5" fill="#fff"/></svg>
  <div class="msg">@hostorion Hostorion site totally down. Even the server status is also down lnk.qv/Q8vT2pXe4N 50 Days ago</div>
  <div class="dots"><span></span><span class="on"></span><span></span></div>
</div>

<footer class="abs footer">
  <div class="col" style="left:136px">
    <div class="f-logo">KB7LUX.io</div>
    <p class="about">Welcome to Maple theme developed for Pressboard and ShopNest theme. So you can get two themes in one package. Also there is paid slider plugins too.</p>
  </div>
  <div class="col" style="left:313px">
    <h4>RECENT POSTS</h4>
    <ul>
      <li>Sonavelle Audio with Post</li><li>Stay ahead of the curve</li><li>Getting Engaged</li><li>Redesigning With Personality</li><li>The Ride of Delmar Okonve</li>
    </ul>
  </div>
  <div class="col" style="left:490px">
    <h4>PHOTO STREAM</h4>
    <div class="thumbs">
      <div role="img" aria-label="Photo of a white interior" style="background:linear-gradient(#ddd,#777)"></div>
      <div role="img" aria-label="Photo of a sunny landscape" style="background:linear-gradient(#8fc3e6,#d8b56a)"></div>
      <div role="img" aria-label="Photo of a teal light tunnel" style="background:radial-gradient(#7fe0d0,#0d3a3a)"></div>
      <div role="img" aria-label="Photo of a blue street scene" style="background:linear-gradient(#3f6f86,#1a2f3a)"></div>
      <div role="img" aria-label="Photo of red and blue abstract shapes" style="background:linear-gradient(135deg,#2a5fb0,#c8262b)"></div>
      <div role="img" aria-label="Photo of a blue sky with clouds" style="background:linear-gradient(#3b74c4,#9cc3e8)"></div>
      <div role="img" aria-label="Photo of a pale misty horizon" style="background:linear-gradient(#c9dce8,#eef3f6)"></div>
      <div role="img" aria-label="Photo of a bright sky over the sea" style="background:linear-gradient(#4f9ad6,#d6ecf8)"></div>
      <div role="img" aria-label="Photo of a blue seascape" style="background:linear-gradient(#8cc6ea,#1b5e96)"></div>
    </div>
  </div>
  <div class="col" style="left:665px">
    <h4>TAGS</h4>
    <div class="tags">
      <div class="tag-row"><span>Agency</span><span>Architecture</span></div>
      <div class="tag-row"><span>Illustration</span><span>Photography</span><span>Print</span></div>
      <div class="tag-row"><span>Technology</span><span>Web Design</span></div>
    </div>
  </div>
</footer>

<div class="abs copy"><p>Copyright 2014 KB7LUX.io. All rights reserved.</p></div>

</body>
</html>
```